Business Card Design Project for Electrical Company

We need a business card designed for a new Electrical Company called Dorvel Electrical Solutions, i dont mind if only Dorvel Electrical is used. We are a domestic and commercial Electrical Company that provides a range of Electrical Services. Our Company colours are Fluro Yellow and Black with the Lightning bolt picture attached.I have attached a card that has been made i think it is rather basic and am looking for something more. the font of Dorvel Electrical has been used on our car graphics as well as the lightning bolt. i want to keep them the same so we can brand our business. Some things we want on the front of the card are Dorvel Electrical Solutions, Owen Platt, 0438516274, admin@dorvelelectrical.example, Lic No 58342, Servicing CQ Region. But we want Owens name seperate to the phone number as its the phone number for the office, owen wont be answering the phone so we are thinking we dont want to give that impression. What do you think? with all that if you have complete different font designs please submit what you think would work best. keeping in mind our company name and details as well as coulors.

Industry/Entity Type

Business

```html
<!DOCTYPE html>
<html lang="en">
<head>
<meta charset="utf-8">
<title>Dorvel Electrical Solutions – Business Card</title>
<link rel="stylesheet" href="https://fonts.googleapis.com/css2?family=Yanone+Kaffeesatz:wght@500&family=Quicksand:wght@600;700&family=Open+Sans:wght@400;700&family=Merriweather:wght@700&family=Lobster+Two:ital,wght@1,700&display=swap">
<style>
  :root {
    --page-bg: #ece7e0;
    --bar-black: #0c0c0c;
    --brand-yellow: #e4ef3c;
    --brand-lime: #d6ea2a;
    --glow-center: #eeae7a;
    --glow-mid: #c98671;
    --glow-edge: #98605f;
    --ink-dark: #2b1f1f;
    --ink-white: #ffffff;
    --chip-grey: #a9a9a9;
  }
  * { box-sizing: border-box; margin: 0; padding: 0; }
  html, body {
    width: 1033px;
    height: 1200px;
    overflow: hidden;
    background: var(--page-bg);
  }
  .card {
    position: absolute;
    left: 25px;
    width: 983px;
    height: 562px;
    background: radial-gradient(ellipse 62% 68% at 50% 42%, var(--glow-center) 0%, var(--glow-mid) 58%, var(--glow-edge) 100%);
    overflow: hidden;
    box-shadow: 0 4px 14px rgba(0,0,0,0.25);
  }
  .card--front { top: 17px; }
  .card--back { top: 622px; }

  .top-bar {
    position: absolute;
    top: 0; left: 0; right: 0;
    height: 37px;
    background: var(--bar-black);
    display: flex;
    justify-content: space-between;
    align-items: center;
    padding: 0 28px;
    font-family: "Yanone Kaffeesatz", sans-serif;
    font-weight: 500;
    font-size: 23px;
    color: var(--brand-yellow);
  }
  .bottom-bar {
    position: absolute;
    bottom: 0; left: 0; right: 0;
    height: 49px;
    background: var(--bar-black);
    display: flex;
    align-items: center;
    justify-content: center;
    font-family: "Quicksand", sans-serif;
    font-weight: 600;
    font-size: 17px;
    letter-spacing: 1px;
    color: var(--ink-white);
  }

  .brand-name {
    position: absolute;
    left: 0; right: 0;
    text-align: center;
    font-family: "Quicksand", sans-serif;
    font-weight: 700;
    color: var(--brand-lime);
    line-height: 1;
    text-transform: uppercase;
  }
  .brand-name span { display: block; }
  .brand-name .line-big { font-size: 46px; }
  .brand-name .line-small { font-size: 30px; margin-top: 4px; }
  .card--front .brand-name { top: 92px; }
  .card--back .brand-name { top: 102px; }

  .contact-chip {
    position: absolute;
    left: 245px;
    height: 23px;
    display: flex;
    align-items: stretch;
    background: var(--ink-white);
    box-shadow: 2px 2px 3px rgba(0,0,0,0.35);
    font-family: Arial, "Open Sans", sans-serif;
    font-size: 14px;
    color: #111;
  }
  .contact-chip .chip-icon {
    width: 30px;
    background: var(--chip-grey);
    display: flex;
    align-items: center;
    justify-content: center;
  }
  .contact-chip .chip-text {
    padding: 0 12px 0 10px;
    display: flex;
    align-items: center;
  }
  .contact-chip--phone { top: 263px; }
  .contact-chip--email { top: 304px; }

  .person {
    position: absolute;
    top: 258px;
    left: 530px;
    width: 280px;
    text-align: right;
  }
  .person-name {
    font-family: "Open Sans", sans-serif;
    font-weight: 700;
    font-size: 36px;
    color: var(--ink-white);
    text-shadow: 2px 2px 3px rgba(0,0,0,0.55);
    line-height: 1.15;
  }
  .person-role {
    font-family: "Lobster Two", cursive;
    font-style: italic;
    font-weight: 700;
    font-size: 16px;
    color: var(--brand-yellow);
    margin-top: 2px;
  }

  .licence {
    position: absolute;
    top: 386px;
    left: 0; right: 0;
    text-align: center;
    font-family: "Open Sans", sans-serif;
    font-size: 23px;
    color: var(--ink-dark);
  }

  .services-title {
    position: absolute;
    top: 260px;
    left: 0; right: 0;
    text-align: center;
    font-family: "Merriweather", serif;
    font-weight: 700;
    font-size: 18px;
    color: #111;
  }
  .service-list {
    position: absolute;
    top: 302px;
    left: 268px;
    display: grid;
    grid-template-columns: 230px 240px;
    row-gap: 23px;
    list-style: none;
    font-family: "Quicksand", sans-serif;
    font-weight: 700;
    font-size: 18px;
    color: #1e1a1a;
  }
  .service-list li {
    display: flex;
    align-items: center;
    gap: 12px;
    height: 27px;
  }
  .service-list svg { flex: none; }
</style>
</head>
<body>

  <section class="card card--front" aria-label="Business card front">
    <header class="top-bar">
      <span>Dorvel Electrical Solutions</span>
      <span>Servicing CQ Region</span>
    </header>

    <div class="brand-name">
      <span class="line-big">Dorvel</span>
      <span class="line-big">Electrical</span>
      <span class="line-small">Solutions</span>
    </div>

    <div class="contact-chip contact-chip--phone">
      <span class="chip-icon">
        <svg width="14" height="12" viewBox="0 0 14 12" aria-hidden="true">
          <path d="M1 4 Q7 0 13 4 L11 5.5 L9.5 4 L4.5 4 L3 5.5 Z" fill="#111"/>
          <rect x="2.5" y="6" width="9" height="5" rx="1" fill="#111"/>
        </svg>
      </span>
      <span class="chip-text">0438516274 (O)</span>
    </div>

    <div class="contact-chip contact-chip--email">
      <span class="chip-icon">
        <svg width="14" height="10" viewBox="0 0 14 10" aria-hidden="true">
          <rect x="0.5" y="0.5" width="13" height="9" fill="#111"/>
          <path d="M0.5 0.5 L7 5.5 L13.5 0.5" fill="none" stroke="#a9a9a9" stroke-width="1"/>
        </svg>
      </span>
      <span class="chip-text">admin@dorvelelectrical.example</span>
    </div>

    <div class="person">
      <p class="person-name">Owen Platt</p>
      <p class="person-role">Licensed Electrician</p>
    </div>

    <p class="licence">Lic No 58342</p>

    <footer class="bottom-bar">www.dorvelelectrical.example</footer>
  </section>

  <section class="card card--back" aria-label="Business card back">
    <header class="top-bar">
      <span>Dorvel Electrical Solutions</span>
      <span>Servicing CQ Region</span>
    </header>

    <div class="brand-name">
      <span class="line-big">Dorvel</span>
      <span class="line-big">Electrical</span>
      <span class="line-small">Solutions</span>
    </div>

    <h2 class="services-title">Our Services</h2>

    <ul class="service-list">
      <li><svg width="14" height="20" viewBox="0 0 14 20" aria-hidden="true"><circle cx="7" cy="7" r="6.5" fill="#f2e83a"/><rect x="4" y="13" width="6" height="5" rx="1" fill="#9a9a9a"/></svg>Light and Power</li>
      <li><svg width="14" height="20" viewBox="0 0 14 20" aria-hidden="true"><circle cx="7" cy="7" r="6.5" fill="#f2e83a"/><rect x="4" y="13" width="6" height="5" rx="1" fill="#9a9a9a"/></svg>Renovations</li>
      <li><svg width="14" height="20" viewBox="0 0 14 20" aria-hidden="true"><circle cx="7" cy="7" r="6.5" fill="#f2e83a"/><rect x="4" y="13" width="6" height="5" rx="1" fill="#9a9a9a"/></svg>TV &amp; Data</li>
      <li><svg width="14" height="20" viewBox="0 0 14 20" aria-hidden="true"><circle cx="7" cy="7" r="6.5" fill="#f2e83a"/><rect x="4" y="13" width="6" height="5" rx="1" fill="#9a9a9a"/></svg>Design &amp; Installation</li>
      <li><svg width="14" height="20" viewBox="0 0 14 20" aria-hidden="true"><circle cx="7" cy="7" r="6.5" fill="#f2e83a"/><rect x="4" y="13" width="6" height="5" rx="1" fill="#9a9a9a"/></svg>Test &amp; Tagging</li>
      <li><svg width="14" height="20" viewBox="0 0 14 20" aria-hidden="true"><circle cx="7" cy="7" r="6.5" fill="#f2e83a"/><rect x="4" y="13" width="6" height="5" rx="1" fill="#9a9a9a"/></svg>Air Con Installation</li>
      <li><svg width="14" height="20" viewBox="0 0 14 20" aria-hidden="true"><circle cx="7" cy="7" r="6.5" fill="#f2e83a"/><rect x="4" y="13" width="6" height="5" rx="1" fill="#9a9a9a"/></svg>Residential</li>
      <li><svg width="14" height="20" viewBox="0 0 14 20" aria-hidden="true"><circle cx="7" cy="7" r="6.5" fill="#f2e83a"/><rect x="4" y="13" width="6" height="5" rx="1" fill="#9a9a9a"/></svg>Smoke Detectors</li>
    </ul>

    <footer class="bottom-bar">www.dorvelelectrical.example</footer>
  </section>

</body>
</html>
```